Tand Works Business Cards

This job is for the design of a business card.
I would like to review the design in 2x colour tones to choose from black and white inverted.
EG:
Black with white logo and white with black logo on BACK
White with black text on front and black with white text options
PRINTING DIMENSIONS: 4.5 x 8.5cm
Complete design will need to be provided in ready to print format with bleed lines
Target Market(s)
The audience of my business are people in the trade industry.
It will be also used for general networking with trades people and possible future clients.
I want to be represented as a professional, dynamic, creative and personable operator.
The card should reflect style, taste, experience, professionalism.
Industry/Entity Type
Business
Requirements
Must have
- BACK CONTENT:
- Logo in white and black background and vice versa with WHITE card and black logo review samples.
- FRONT CARD CONTENT:
- Name: Nico Havelmor
- Director
- Phone: 0472 816 094
- Email: nico@tandworks.com.au
- Web: tandworks.com.au
- LICENCE #: KR-T 57264
Nice to have
- Possibly a textured background design on rear as a pose to a solid black
- Possibly adding a blue or orange discreet colour tone (possibly for email, phone abbreviated letter or symbols).

```html
<!DOCTYPE html>
<html lang="en">
<head>
<meta charset="utf-8">
<title>Tand Works Business Cards</title>
<link rel="stylesheet" href="https://fonts.googleapis.com/css2?family=Arimo:wght@400;700&display=swap">
<style>
  :root {
    --stage: #3b3b3c;
    --card: #151515;
    --card-edge: #1d1d1d;
    --ink: #6f6f70;
    --ink-strong: #8a8a8b;
    --ink-faint: #262626;
    --rule: #4a4a4b;
  }
  * { box-sizing: border-box; margin: 0; padding: 0; }
  html, body {
    width: 1200px; height: 835px; overflow: hidden;
    background: var(--stage);
    font-family: "Arimo", Arial, sans-serif;
  }
  .stage {
    position: relative; width: 1200px; height: 835px;
    display: flex; align-items: center; justify-content: center; gap: 60px;
  }
  .card {
    position: relative; width: 510px; height: 270px;
    background: var(--card);
    border: 1px solid var(--card-edge);
    box-shadow: 0 18px 40px rgba(0,0,0,.45);
    overflow: hidden;
  }
  .card--back {
    background: radial-gradient(ellipse at 35% 30%, #1c1c1c 0%, var(--card) 70%);
    display: flex; align-items: center; justify-content: center;
  }
  .back-name {
    font-size: 46px; font-weight: 400; letter-spacing: 2px;
    text-transform: uppercase; color: var(--ink-faint); line-height: 1;
  }
  .brand {
    position: absolute; top: 36px; right: 40px;
    font-size: 40px; font-weight: 400; letter-spacing: 1px;
    color: var(--ink-strong); text-transform: uppercase; line-height: 1;
  }
  .person { position: absolute; left: 40px; top: 118px; color: var(--ink); }
  .person__name { font-size: 14px; font-weight: 700; text-transform: uppercase; letter-spacing: .5px; }
  .person__role { font-size: 13px; margin-top: 2px; }
  .rule { position: absolute; left: 40px; right: 40px; height: 1px; background: var(--rule); }
  .rule--top { top: 166px; }
  .rule--bottom { top: 226px; }
  .contacts {
    position: absolute; left: 40px; top: 178px;
    display: flex; gap: 26px; align-items: center;
    font-size: 13px; color: var(--ink);
  }
  .contact { display: flex; align-items: center; gap: 7px; }
  .contact svg, .web svg { width: 13px; height: 13px; fill: none; stroke: var(--ink); stroke-width: 1.4; }
  .licence { position: absolute; right: 40px; top: 204px; font-size: 12px; color: var(--ink); }
  .web {
    position: absolute; right: 40px; top: 238px;
    display: flex; align-items: center; gap: 7px; font-size: 13px; color: var(--ink);
  }
</style>
</head>
<body>
<main class="stage">
  <section class="card card--back" aria-label="Card back, textured black with tone-on-tone company name">
    <p class="back-name">Tand Works</p>
  </section>

  <section class="card card--front" aria-label="Card front">
    <p class="brand">Tand Works</p>

    <div class="person">
      <p class="person__name">Nico Havelmor</p>
      <p class="person__role">Director</p>
    </div>

    <div class="rule rule--top"></div>

    <div class="contacts">
      <span class="contact">
        <svg viewBox="0 0 14 14"><rect x="3" y="1" width="8" height="12" rx="1.5"/><line x1="6" y1="11" x2="8" y2="11"/></svg>
        0472 816 094
      </span>
      <span class="contact">
        <svg viewBox="0 0 14 14"><rect x="1" y="3" width="12" height="8"/><polyline points="1,3 7,8 13,3"/></svg>
        nico@tandworks.com.au
      </span>
    </div>

    <p class="licence">Licence #: KR-T 57264</p>

    <div class="rule rule--bottom"></div>

    <div class="web">
      <svg viewBox="0 0 14 14"><circle cx="7" cy="7" r="6"/><ellipse cx="7" cy="7" rx="2.6" ry="6"/><line x1="1" y1="7" x2="13" y2="7"/></svg>
      www.tandworks.com.au
    </div>
  </section>
</main>
</body>
</html>
```